BRCW Business Cards

Business Cards should contain:
Bright Ridgecrest Coating Works
Felix Darrow
M: 0417 865 093
E: brightRCW@fernpost.example
BRCW logo
TCG logo
Painting & Decorating
Licence # 719362K
slogan: See the Shine of Careful Craft Work

Target Market(s)

all aspect of painting

Industry/Entity Type

Trade

Contact Information for Business Card

Felix Darrow
M: 0417 865 093
E: brightRCW@fernpost.example
BRCW logo
TCG logo
Painting & Decorating
Licence # 719362K

Font styles to use
Serif
Sans Serif

Requirements
Must have
• clear design with nice backround
• two sides
• smal TCG logo
Nice to have
• easy to read
Should not have
• mess
• black
• plastics form

```html
<!DOCTYPE html>
<html lang="en">
<head>
<meta charset="utf-8">
<title>BRCW Business Cards</title>
<link rel="stylesheet" href="https://fonts.googleapis.com/css2?family=Libre+Caslon+Text:wght@400&family=Open+Sans:wght@400&display=swap">
<style>
  :root {
    --page: #ffffff;
    --ink: #1c1c1c;
    --brand-teal: #17504a;
    --partner-navy: #24408f;
    --frame: #111111;
    --wash-peach: rgba(248, 176, 140, 0.45);
    --wash-lime: rgba(214, 236, 150, 0.5);
    --wash-lilac: rgba(206, 176, 230, 0.45);
    --wash-sky: rgba(168, 206, 236, 0.5);
    --wash-mint: rgba(190, 232, 196, 0.45);
    --wash-base: #fbfaf1;
  }
  html, body {
    margin: 0;
    padding: 0;
    width: 1200px;
    height: 1200px;
    overflow: hidden;
    background: var(--page);
  }
  .canvas {
    position: relative;
    width: 1200px;
    height: 1200px;
  }
  .card {
    position: absolute;
    left: 180px;
    width: 838px;
    height: 478px;
    border: 1px solid var(--frame);
    overflow: hidden;
    font-family: "Open Sans", Verdana, sans-serif;
    color: var(--ink);
  }
  .card--front { top: 96px; }
  .card--back { top: 610px; }

  .paint-wash {
    position: absolute;
    inset: 0;
    background:
      radial-gradient(ellipse 180px 140px at 12% 18%, var(--wash-peach), transparent 70%),
      radial-gradient(ellipse 160px 200px at 8% 70%, var(--wash-peach), transparent 70%),
      radial-gradient(ellipse 220px 160px at 35% 75%, var(--wash-mint), transparent 70%),
      radial-gradient(ellipse 200px 150px at 55% 15%, var(--wash-lime), transparent 70%),
      radial-gradient(ellipse 200px 170px at 62% 55%, var(--wash-lilac), transparent 70%),
      radial-gradient(ellipse 170px 140px at 50% 92%, var(--wash-lilac), transparent 70%),
      radial-gradient(ellipse 220px 180px at 90% 30%, var(--wash-sky), transparent 70%),
      radial-gradient(ellipse 200px 160px at 85% 85%, var(--wash-lime), transparent 70%),
      radial-gradient(ellipse 140px 120px at 28% 40%, var(--wash-peach), transparent 70%),
      var(--wash-base);
  }

  .brand-mark {
    position: absolute;
    border-radius: 50%;
    background: var(--brand-teal);
  }
  .brand-divider {
    position: absolute;
    width: 2px;
    background: var(--brand-teal);
  }
  .brand-name,
  .brand-tagline {
    position: absolute;
    margin: 0;
    font-family: "Libre Caslon Text", Georgia, serif;
    font-weight: 400;
    color: var(--brand-teal);
    line-height: 1;
    white-space: nowrap;
  }

  /* front */
  .card--front .brand-mark { left: 172px; top: 164px; width: 128px; height: 128px; }
  .card--front .brand-divider { left: 318px; top: 116px; height: 236px; }
  .card--front .brand-name { left: 338px; top: 138px; font-size: 100px; letter-spacing: 1px; }
  .card--front .brand-tagline { left: 342px; top: 236px; font-size: 39px; line-height: 1.33; }

  /* back */
  .contact {
    position: absolute;
    left: 48px;
    margin: 0;
    font-weight: 400;
    line-height: 1.05;
    white-space: nowrap;
  }
  .contact__name { top: 34px; font-size: 56px; }
  .contact__lines { top: 134px; font-size: 34px; }
  .contact__licence { top: 236px; font-size: 34px; }

  .card--back .brand-mark { left: 584px; top: 118px; width: 52px; height: 52px; }
  .card--back .brand-divider { left: 646px; top: 90px; height: 104px; }
  .card--back .brand-name { left: 656px; top: 96px; font-size: 42px; }
  .card--back .brand-tagline { left: 656px; top: 146px; font-size: 16px; line-height: 1.4; }

  .partner {
    position: absolute;
    left: 630px;
    top: 280px;
    width: 138px;
    display: flex;
    align-items: center;
    justify-content: center;
    gap: 12px;
  }
  .partner__square {
    width: 34px;
    height: 34px;
    background: var(--partner-navy);
  }
  .partner__name {
    font-family: "Open Sans", Verdana, sans-serif;
    font-size: 34px;
    color: var(--partner-navy);
    line-height: 1;
  }

  .slogan {
    position: absolute;
    left: 0;
    right: 0;
    top: 404px;
    margin: 0;
    text-align: center;
    font-size: 28px;
    line-height: 1;
  }
</style>
</head>
<body>
<main class="canvas">

  <section class="card card--front">
    <div class="paint-wash" role="img" aria-label="Soft pastel watercolour paint splashes in peach, lime, lilac and sky blue"></div>
    <div class="brand-mark"></div>
    <div class="brand-divider"></div>
    <h1 class="brand-name">BRCW</h1>
    <p class="brand-tagline">Bright Ridgecrest<br>Coating Works</p>
  </section>

  <section class="card card--back">
    <div class="paint-wash" role="img" aria-label="Soft pastel watercolour paint splashes in peach, lime, lilac and sky blue"></div>

    <h2 class="contact contact__name">Felix Darrow</h2>
    <p class="contact contact__lines">M: 0417 865 093<br>E: brightRCW@fernpost.example</p>
    <p class="contact contact__licence">Painting &amp; Decorating<br>Licence # 719362K</p>

    <div class="brand-mark"></div>
    <div class="brand-divider"></div>
    <p class="brand-name">BRCW</p>
    <p class="brand-tagline">Bright Ridgecrest<br>Coating Works</p>

    <div class="partner">
      <span class="partner__square"></span>
      <span class="partner__name">TCG</span>
    </div>

    <p class="slogan">“See the Shine of Careful Craft Work”</p>
  </section>

</main>
</body>
</html>
```